Carpet and Flooring business needs a leaflet/flyer design

Brackenridge Floors is a small carpet and flooring business looking for a flyer to be printed on double sided A6 postcard. As a home based business the flyer is to inform local people of our existence, our services and our ability to genuinely save them money. (We dont do gimmicks and fake sales!). As this flyer will be delivered to mainly households it should be more carpet than flooring.

How we operate as a home based business is that once we receive a call from a potential customer we try and discover a bit more about their requirements and budget, we then arrange to visit them to measure up and to show them a selection of samples based on the initial call. Normally we get this right first time, if not we will return at a later date with more samples. We then give the quote and hopefully get the order.

We sell all the makes and ranges you will find in the shops but for a lot less. We do all qualities from entry level (7.99M2) to top end. We do not however get involved with 'cheap carpets'.... these so called carpets offer a false economy and don't do our reputation any good.

Target Market(s)

home owners, landlords, estate agents, people that need carpet

Industry/Entity Type

Flooring

Requirements
Must have
• Phone Number - 01432 517804
Nice to have
• more emphasise on carpets

local
honest
reliable
experienced
professional
friendly
value for money

Should not have
• No mention of 'cheap carpets'
No cartoon characters carrying a roll of carpet.
No flying or magic carpets.

```html
<!DOCTYPE html>
<html lang="en">
<head>
<meta charset="utf-8">
<title>Brackenridge Floors – A6 Postcard</title>
<link rel="stylesheet" href="https://fonts.googleapis.com/css2?family=Anton&family=Oswald:wght@500;600;700&family=Parisienne&family=Questrial&family=Michroma&display=swap">
<style>
  :root {
    --backdrop: #a3b0ae;
    --orange: #f26b3a;
    --green: #a6d44e;
    --grey: #a8b3b1;
    --black: #000000;
    --white: #ffffff;
    --yellow: #f8ec1c;
  }
  html, body {
    margin: 0;
    padding: 0;
    width: 882px;
    height: 1200px;
    overflow: hidden;
    background: var(--backdrop);
  }
  .sheet {
    position: relative;
    width: 882px;
    height: 1200px;
  }
  .card {
    position: absolute;
    left: 87px;
    width: 724px;
    height: 514px;
    display: block;
    filter: drop-shadow(3px 6px 5px rgba(0,0,0,0.35));
  }
  .card--front { top: 48px; }
  .card--rear { top: 636px; }
  .side-label {
    position: absolute;
    right: 70px;
    margin: 0;
    font-family: "Michroma", sans-serif;
    font-size: 19px;
    font-weight: 700;
    color: var(--black);
  }
  .side-label--front { top: 572px; }
  .side-label--rear { top: 1160px; }

  .card-edge { fill: var(--white); stroke: var(--black); stroke-width: 2; }
  .swoosh { fill: var(--green); }
  .panel { fill: var(--black); }
  .mark { fill: var(--orange); }

  .tagline { font-family: "Parisienne", cursive; font-size: 36px; fill: var(--orange); }
  .brand-name { font-family: "Oswald", sans-serif; font-weight: 700; fill: var(--orange); }
  .brand-name--panel { fill: var(--green); }
  .selling-point { font-family: "Oswald", sans-serif; font-weight: 700; font-size: 28px; fill: var(--black); }
  .headline { font-family: "Anton", sans-serif; font-size: 100px; fill: var(--white); }

  .service-type { font-family: "Oswald", sans-serif; font-weight: 600; font-size: 19px; }
  .service-type--green { fill: var(--green); }
  .service-type--orange { fill: var(--orange); }
  .service-type--grey { fill: var(--grey); }

  .offer-shadow { fill: var(--black); }
  .offer--green { fill: var(--green); }
  .offer--orange { fill: var(--orange); }
  .offer--grey { fill: var(--grey); }
  .offer-label { font-family: "Oswald", sans-serif; font-weight: 700; font-size: 27px; fill: var(--white); }

  .promise { font-family: "Oswald", sans-serif; font-weight: 500; font-size: 17px; fill: var(--white); }
  .call-line { font-family: "Questrial", sans-serif; fill: var(--yellow); }
  .phone { font-family: "Questrial", sans-serif; font-weight: 700; fill: var(--yellow); stroke: var(--yellow); stroke-width: 1.5; }
</style>
</head>
<body>
<main class="sheet">

  <!-- Front side -->
  <svg class="card card--front" viewBox="0 0 873 620" preserveAspectRatio="none" aria-label="Postcard front">
    <rect class="card-edge" x="1" y="1" width="871" height="618"/>
    <path class="swoosh" d="M860 0 Q330 200 328 619 L872 619 L872 0 Z"/>
    <path class="panel" d="M872 4 Q392 232 376 619 L872 619 Z"/>

    <text class="tagline" x="20" y="46">Why spend more than you have to on your next carpet!</text>

    <rect class="mark" x="40" y="140" width="56" height="56"/>
    <text class="brand-name" x="112" y="172" font-size="48">Brackenridge</text>
    <text class="brand-name" x="112" y="230" font-size="48">Floors</text>

    <text class="selling-point" x="25" y="288">YOUR LOCAL CARPET &amp;</text>
    <text class="selling-point" x="25" y="319">FLOORING SPECIALIST</text>
    <text class="selling-point" x="170" y="380" text-anchor="middle">OFFERING YOU VALUE</text>
    <text class="selling-point" x="170" y="411" text-anchor="middle">FOR MONEY</text>
    <text class="selling-point" x="170" y="472" text-anchor="middle">PROFESSIONAL</text>
    <text class="selling-point" x="170" y="503" text-anchor="middle">FRIENDLY SERVICE</text>
    <text class="selling-point" x="166" y="564" text-anchor="middle">OVER 27 YEARS OF</text>
    <text class="selling-point" x="166" y="595" text-anchor="middle">EXPERIENCE</text>

    <rect class="mark" x="610" y="188" width="18" height="18"/>
    <text class="brand-name brand-name--panel" x="636" y="206" font-size="24" textLength="204" lengthAdjust="spacingAndGlyphs">Brackenridge Floors</text>

    <text class="headline" x="516" y="352" textLength="320" lengthAdjust="spacingAndGlyphs">We Can</text>
    <text class="headline" x="436" y="468" textLength="400" lengthAdjust="spacingAndGlyphs">Save YOU</text>
    <text class="headline" x="400" y="582" textLength="436" lengthAdjust="spacingAndGlyphs">££££££’s</text>
  </svg>
  <p class="side-label side-label--front">Front</p>

  <!-- Rear side -->
  <svg class="card card--rear" viewBox="0 0 873 620" preserveAspectRatio="none" aria-label="Postcard rear">
    <rect class="card-edge" x="1" y="1" width="871" height="618"/>
    <path class="swoosh" d="M868 0 C450 110 270 260 322 619 L872 619 L872 0 Z"/>
    <path class="panel" d="M872 8 C480 110 320 250 372 619 L872 619 Z"/>

    <text class="service-type service-type--green" x="24" y="34">Contract &amp; Domestic</text>
    <text class="service-type service-type--orange" x="233" y="34">Commercial &amp; Residential</text>
    <text class="service-type service-type--grey" x="489" y="34">Carpet &amp; Flooring Service</text>

    <rect class="mark" x="40" y="140" width="56" height="56"/>
    <text class="brand-name" x="112" y="172" font-size="48">Brackenridge</text>
    <text class="brand-name" x="112" y="230" font-size="48">Floors</text>

    <g class="offers">
      <polygon class="offer-shadow" points="24,311 160,273 298,311 160,351"/>
      <polygon class="offer--green" points="24,300 160,262 298,300 160,340"/>
      <text class="offer-label" x="160" y="310" text-anchor="middle">Free Advice</text>

      <polygon class="offer-shadow" points="24,393 160,355 298,393 160,433"/>
      <polygon class="offer--orange" points="24,382 160,344 298,382 160,422"/>
      <text class="offer-label" x="160" y="392" text-anchor="middle">Free Measuring</text>

      <polygon class="offer-shadow" points="24,474 160,436 298,474 160,514"/>
      <polygon class="offer--grey" points="24,463 160,425 298,463 160,503"/>
      <text class="offer-label" x="160" y="473" text-anchor="middle">Free Estimates</text>

      <polygon class="offer-shadow" points="24,556 160,518 298,556 160,596"/>
      <polygon class="offer--orange" points="24,545 160,507 298,545 160,585"/>
      <text class="offer-label" x="160" y="555" text-anchor="middle">No Obligation</text>
    </g>

    <rect class="mark" x="690" y="114" width="12" height="12"/>
    <text class="brand-name brand-name--panel" x="708" y="126" font-size="17" textLength="140" lengthAdjust="spacingAndGlyphs">Brackenridge Floors</text>

    <text class="promise" x="848" y="190" text-anchor="end">We come to you with a range of samples.</text>
    <text class="promise" x="845" y="236" text-anchor="end">All leading makes supplied.</text>
    <text class="promise" x="845" y="281" text-anchor="end">The price we quote is the price you pay,</text>
    <text class="promise" x="845" y="304" text-anchor="end">No gimmicks and No misleading special offers.</text>
    <text class="promise" x="845" y="349" text-anchor="end">All our installations are carried out to the highest standard.</text>
    <text class="promise" x="845" y="394" text-anchor="end">We can move your furniture and uplift old flooring if required.</text>
    <text class="promise" x="848" y="439" text-anchor="end">You pay the balance only when the work is complete and you are</text>
    <text class="promise" x="848" y="462" text-anchor="end">entirely satisfied.</text>

    <text class="call-line" x="848" y="518" font-size="40" text-anchor="end">call us today on</text>
    <text class="phone" x="403" y="576" font-size="56" textLength="445" lengthAdjust="spacingAndGlyphs">01432 517804</text>
    <text class="call-line" x="848" y="604" font-size="26" text-anchor="end">to make your appointment</text>
  </svg>
  <p class="side-label side-label--rear">Rear</p>

</main>
</body>
</html>
```